Dennis J. Halvorsen stationery and new logo

Create Word template stationery, with a logo, for a Forensic Psychiatry business.

The stationery must include contact info (see below)

The logo should include images similar to (but not necessarily identical to) the ones in the uploaded document. They are the scales of justice and the caduceus, or staff, associated with medicine.

Target Market(s)

consumers of forensic psychiatry (usually lawyers and their clients)

Industry/Entity Type

Mental Health

Logo Text

Dennis J. Halvorsen, MD, DLFAPA

Font styles to use
Serif

Colors

Designer to choose colors to be used in the design.

Requirements
Must have
• Forensic Psychiatry
• 735 N. Birch Street
• M Building
• East Marlow, PA 19487
• (484) 517-3862
Nice to have
• Conservative color scheme

```html
<!DOCTYPE html>
<html lang="en">
<head>
<meta charset="utf-8">
<title>Dennis J. Halvorsen – Stationery</title>
<link rel="stylesheet" href="https://fonts.googleapis.com/css2?family=Gelasio:wght@400;500&family=PT+Sans:wght@400;700&display=swap">
<style>
  :root {
    --navy: #0b3d6e;
    --backdrop: #d3d3d5;
    --paper: #ffffff;
    --body-grey: #a3a3a3;
    --ink: #1a1a1a;
    --faint: #ececec;
  }
  * { margin: 0; padding: 0; box-sizing: border-box; }
  html, body { width: 1200px; height: 960px; overflow: hidden; background: var(--backdrop); }
  .canvas { position: relative; width: 1200px; height: 960px; font-family: "PT Sans", sans-serif; }
  .sheet { position: absolute; background: var(--paper); box-shadow: 0 2px 6px rgba(0,0,0,.28); overflow: hidden; }
  .serif { font-family: "Gelasio", serif; color: var(--navy); }

  /* master logo */
  .brand-main { position: absolute; left: 650px; top: 48px; width: 480px; text-align: center; }
  .brand-main .mark { width: 64px; height: 64px; border-radius: 50%; background: var(--navy); margin: 70px auto 28px; }
  .brand-main .name { font-size: 47px; line-height: 1; }
  .brand-main .creds { font-size: 37px; line-height: 1; margin-top: 18px; }

  /* letterhead */
  .letterhead { left: 24px; top: 216px; width: 549px; height: 710px; }
  .letterhead .head { position: absolute; left: 0; right: 0; top: 28px; text-align: center; }
  .letterhead .mark { width: 30px; height: 30px; border-radius: 50%; background: var(--navy); margin: 12px auto 14px; }
  .letterhead .name { font-size: 17px; line-height: 1.1; }
  .letterhead .creds { font-size: 12px; font-weight: 500; margin-top: 3px; }
  .salutation { position: absolute; left: 47px; top: 197px; font-size: 9.5px; color: var(--body-grey); }
  .letter-body { position: absolute; left: 35px; top: 240px; width: 480px; font-size: 9.6px; line-height: 12.9px; color: var(--body-grey); text-align: justify; }
  .letter-body p { margin-bottom: 12.9px; }
  .letter-body p:first-child { text-indent: 32px; }
  .contact { position: absolute; font-size: 8px; line-height: 11.2px; color: var(--ink); }
  .letterhead .contact { left: 35px; top: 631px; }
  .contact .dept, .letterhead .contact .phone { color: var(--navy); }
  .band { position: absolute; left: 0; right: 0; bottom: 0; height: 18px; background: var(--navy); }

  /* envelope back */
  .envelope { left: 594px; top: 390px; width: 582px; height: 258px; }
  .flap { position: absolute; left: 0; right: 0; top: 0; height: 57px; background: var(--navy); border-radius: 0 0 24px 24px; display: flex; align-items: center; justify-content: center; gap: 8px; }
  .flap .mark { width: 10px; height: 10px; border-radius: 50%; background: var(--paper); }
  .flap .name { font-family: "Gelasio", serif; font-size: 11px; color: var(--paper); }

  /* envelope front */
  .envelope-front { left: 594px; top: 664px; width: 582px; height: 258px; }
  .envelope-front .head { position: absolute; left: 12px; width: 114px; top: 18px; text-align: center; }
  .envelope-front .mark { width: 26px; height: 26px; border-radius: 50%; background: var(--navy); margin: 4px auto 10px; }
  .envelope-front .name { font-size: 11.5px; line-height: 1.1; }
  .envelope-front .creds { font-size: 9.5px; font-weight: 500; margin-top: 1px; }
  .envelope-front .contact { left: 23px; top: 181px; line-height: 10.5px; }
  .envelope-front .contact .dept { color: var(--ink); }
  .envelope-front .phone { margin-top: 3px; }
  .faint-mark { position: absolute; left: 330px; top: 26px; width: 200px; height: 200px; border-radius: 50%; border: 10px solid var(--faint); display: flex; align-items: center; justify-content: center; }
  .faint-mark span { font-family: "Gelasio", serif; font-size: 17px; color: var(--faint); }
</style>
</head>
<body>
<div class="canvas">

  <div class="brand-main serif">
    <div class="mark"></div>
    <div class="name">Dennis J. Halvorsen</div>
    <div class="creds">MD, DLFAPA</div>
  </div>

  <section class="sheet letterhead">
    <header class="head serif">
      <div class="mark"></div>
      <div class="name">Dennis J. Halvorsen</div>
      <div class="creds">MD, DLFAPA</div>
    </header>
    <p class="salutation">Dear Sir</p>
    <div class="letter-body">
      <p>Lorem ipsum dolor sit amet, consectetur adipiscing elit. Integer eu odio mattis, pulvinar turpis quis, faucibus nisl. Proin feugiat, erat vitae cursus pharetra, enim est semper ligula, in malesuada orci nisl et diam. Etiam elementum metus ac fringilla vulputate. Etiam mattis ligula sed ante mollis bibendum. Orci varius natoque penatibus et magnis dis parturient montes, nascetur ridiculus mus.</p>
      <p>Ut nibh augue, blandit ac orci ac, rutrum congue enim. Suspendisse gravida vulputate felis, quis interdum orci tincidunt quis. Praesent imperdiet maximus neque. Mauris ut dui enim. Nullam at efficitur elit. Donec ante ipsum, fermentum at lectus vel, blandit vulputate ante. Proin luctus suscipit diam id vestibulum. Morbi malesuada id mauris eget ullamcorper.</p>
      <p>Donec varius orci purus, vitae aliquam libero volutpat id. Integer sed imperdiet libero. Aliquam accumsan, risus sit amet ornare consectetur, turpis felis dictum justo, non rhoncus mauris dui sed velit. Pellentesque habitant morbi tristique senectus et netus et malesuada fames ac turpis egestas. Pellentesque tincidunt vitae ligula nec imperdiet. Donec sed congue enim. Nullam elementum faucibus nulla nec vestibulum. Sed at tempor ligula. In quis vulputate nunc. Integer at gravida lacus, ac tristique risus. Sed at vulputate nulla.</p>
      <p>Praesent blandit nunc eu efficitur commodo. In tempor nisi ex, vel venenatis ante vestibulum a. Duis vestibulum nibh a erat sagittis, nec euismod lorem varius. Nam ultricies turpis sed justo sollicitudin volutpat. Morbi sed mollis eros. Sed quis tortor id enim vehicula porttitor. Curabitur non aliquam ex. Phasellus dignissim fermentum elit, at finibus ligula mattis eget.</p>
    </div>
    <address class="contact" style="font-style:normal">
      <div class="dept">Forensic Psychiatry</div>
      <div>735 N. Birch Street, M Building</div>
      <div>East Marlow, PA 19487</div>
      <div class="phone">(484) 517-3862</div>
    </address>
    <div class="band"></div>
  </section>

  <section class="sheet envelope">
    <div class="flap">
      <div class="mark"></div>
      <span class="name">Dennis J. Halvorsen</span>
    </div>
  </section>

  <section class="sheet envelope-front">
    <div class="faint-mark" role="img" aria-label="Faint background brand mark"><span>Dennis J. Halvorsen</span></div>
    <header class="head serif">
      <div class="mark"></div>
      <div class="name">Dennis J. Halvorsen</div>
      <div class="creds">MD, DLFAPA</div>
    </header>
    <address class="contact" style="font-style:normal">
      <div class="dept">Forensic Psychiatry</div>
      <div>735 N. Birch Street</div>
      <div>M Building</div>
      <div>East Marlow, PA 19487</div>
      <div class="phone">(484) 517-3862</div>
    </address>
    <div class="band"></div>
  </section>

</div>
</body>
</html>
```